Lantern Business Cards

Need business cards for my employees at my restaurant.

Needs to include:
Our Logo
Lantern Bowls & Brews
Name: Nora Pettigrew
Title : Owner
Address: 487 Mirella Ave. Marlow Springs, NM 86519
Web: www.lanternkestrel.com
Phone: 928-555-0147
Cell: 928-555-0192
Email: info@lanternkestrel.com

```html
<!DOCTYPE html>
<html lang="en">
<head>
<meta charset="utf-8">
<title>Lantern Bowls &amp; Brews — Business Cards</title>
<link rel="stylesheet" href="https://fonts.googleapis.com/css2?family=Poppins:wght@400;500;700&display=swap">
<style>
  :root {
    --brand-red: #c0202f;
    --ink: #0b0b0b;
    --paper: #ffffff;
    --backdrop: #e6e6e6;
    --muted: #222222;
  }
  * { box-sizing: border-box; margin: 0; padding: 0; }
  html, body { width: 1200px; height: 1200px; overflow: hidden; }
  body {
    background: var(--backdrop);
    font-family: "Poppins", Arial, sans-serif;
    position: relative;
  }
  .card {
    position: absolute;
    left: 150px;
    width: 900px;
    height: 516px;
    background: var(--paper);
    overflow: hidden;
  }
  .card--front { top: 84px; }
  .card--back { top: 628px; }
  .card__shapes { position: absolute; inset: 0; width: 900px; height: 516px; }

  .holder { position: absolute; left: 60px; top: 76px; }
  .holder__name {
    color: var(--brand-red);
    font-weight: 700;
    font-size: 40px;
    line-height: 1;
    letter-spacing: 0.3px;
    text-transform: uppercase;
  }
  .holder__title {
    color: var(--muted);
    font-size: 27px;
    font-weight: 400;
    margin-top: 6px;
  }

  .brand {
    position: absolute;
    display: flex;
    align-items: center;
    gap: 16px;
    color: var(--brand-red);
    font-weight: 700;
    text-transform: uppercase;
    line-height: 1;
  }
  .brand__dot { border-radius: 50%; background: var(--brand-red); flex: none; }
  .card--front .brand { left: 548px; top: 176px; font-size: 52px; }
  .card--front .brand__dot { width: 44px; height: 44px; }
  .card--back .brand { left: 240px; top: 146px; font-size: 76px; }
  .card--back .brand__dot { width: 64px; height: 64px; }

  .contact { position: absolute; left: 58px; top: 252px; list-style: none; }
  .contact__item {
    display: flex;
    align-items: center;
    gap: 18px;
    height: 43px;
    color: var(--paper);
    font-size: 24px;
    font-weight: 400;
  }
  .contact__icon { width: 18px; height: 18px; flex: none; }

  .tagline {
    position: absolute;
    left: 0; width: 904px;
    top: 412px;
    text-align: center;
    color: var(--paper);
    font-weight: 700;
    font-size: 33px;
    letter-spacing: 0.3px;
    text-transform: uppercase;
  }
</style>
</head>
<body>

<section class="card card--front" aria-label="Business card front">
  <svg class="card__shapes" viewBox="0 0 900 516" aria-hidden="true">
    <path d="M0 209 H290 Q310 209 322 224 H0 Z" fill="var(--brand-red)"/>
    <path d="M0 224 H380 Q400 224 414 240 L462 300 Q478 322 505 324 H640 Q680 324 700 355 H900 V516 H0 Z" fill="var(--ink)"/>
    <path d="M484 305 H715 Q730 305 724 318 L710 355 Q702 361 690 361 H540 Q510 358 484 305 Z" fill="var(--brand-red)"/>
    <path d="M702 324 H800 Q820 324 830 340 L842 355 H710 Z" fill="var(--ink)"/>
  </svg>

  <div class="holder">
    <h1 class="holder__name">Nora Pettigrew</h1>
    <p class="holder__title">Owner</p>
  </div>

  <div class="brand"><span class="brand__dot"></span><span>Lantern</span></div>

  <ul class="contact">
    <li class="contact__item">
      <svg class="contact__icon" viewBox="0 0 24 24"><path fill="var(--brand-red)" d="M6.6 10.8a15 15 0 0 0 6.6 6.6l2.2-2.2a1 1 0 0 1 1-.25 11.4 11.4 0 0 0 3.6.57 1 1 0 0 1 1 1V20a1 1 0 0 1-1 1A17 17 0 0 1 3 4a1 1 0 0 1 1-1h3.5a1 1 0 0 1 1 1c0 1.25.2 2.45.57 3.57a1 1 0 0 1-.25 1z"/></svg>
      <span>928-555-0147</span>
    </li>
    <li class="contact__item">
      <svg class="contact__icon" viewBox="0 0 24 24"><rect x="6" y="1.5" width="12" height="21" rx="2.5" fill="none" stroke="var(--brand-red)" stroke-width="2.4"/><circle cx="12" cy="18.5" r="1.3" fill="var(--brand-red)"/></svg>
      <span>928-555-0192</span>
    </li>
    <li class="contact__item">
      <svg class="contact__icon" viewBox="0 0 24 24"><rect x="1.5" y="4" width="21" height="16" rx="2" fill="var(--brand-red)"/><path d="M3 6l9 7 9-7" fill="none" stroke="var(--ink)" stroke-width="2"/></svg>
      <span>info@lanternkestrel.com</span>
    </li>
    <li class="contact__item">
      <svg class="contact__icon" viewBox="0 0 24 24"><circle cx="12" cy="12" r="10" fill="none" stroke="var(--brand-red)" stroke-width="2.4"/><path d="M2 12h20M12 2c3 3 3 17 0 20M12 2c-3 3-3 17 0 20" fill="none" stroke="var(--brand-red)" stroke-width="1.8"/></svg>
      <span>www.lanternkestrel.com</span>
    </li>
    <li class="contact__item">
      <svg class="contact__icon" viewBox="0 0 24 24"><path fill="var(--brand-red)" d="M12 1a8 8 0 0 0-8 8c0 6 8 14 8 14s8-8 8-14a8 8 0 0 0-8-8zm0 11a3 3 0 1 1 0-6 3 3 0 0 1 0 6z"/></svg>
      <span>487 Mirella Ave. Marlow Springs, NM 86519</span>
    </li>
  </ul>
</section>

<section class="card card--back" aria-label="Business card back">
  <svg class="card__shapes" viewBox="0 0 900 516" aria-hidden="true">
    <path d="M524 312 Q528 298 544 298 H900 V378 H514 Z" fill="var(--brand-red)"/>
    <path d="M0 330 H572 Q592 330 592 345 Q592 360 572 360 H0 Z" fill="var(--ink)"/>
    <path d="M0 492 L80 392 Q96 360 128 360 H770 Q800 360 812 382 L900 490 V516 H0 Z" fill="var(--paper)"/>
    <path d="M0 516 V500 L88 398 Q102 368 132 368 H766 Q792 368 802 388 L900 510 V516 Z" fill="var(--brand-red)"/>
  </svg>

  <div class="brand"><span class="brand__dot"></span><span>Lantern</span></div>

  <p class="tagline">Lantern Bowls &amp; Brews</p>
</section>

</body>
</html>
```